Vantro Baseball Athletic Training Brochure Design 3 Fold 8x8

I need to create a New 3 page folding brochure for an elite baseball training company that focuses on all aspects of becoming a better baseball player through athletic training. I would like it to be fresh and new. My client likes the Harbor City Comets colors. It needs to appeal to a young athletic crowd.

HERE IS A WEBSITE FROM A COMPETITOR
https://www.plinthrow.example/baseball/
I HAVE INCLUEDE A PDF FLYER OF SOMETHING THEIR COMPETITORS HAVE DONE

Target Market(s)

Professional and amateur baseball players

Font styles to use
Sans Serif

Colors
33a6d7
3176b5
000000
b2b2b2

Requirements
Must have
• Images featuring training. I would use KELBAFORM training images as well.
• References:
• "As a former professional baseball player, I know the hard work and dedication it takes to make it and be your best.
• Every athlete that aspires to be the best they can be must out work their opponents on all levels,
• especially when it comes to taking care of your body. Being strong physically is a must with all the
• elite athletes competing. To get an edge, you have to be on a program designed by en experienced trainer
• and leader. With that said, there's nobody I'd recommend higher than Dale Vantrock with Vantro's
• Training.
• -Corbin Pask
• Founder Hollow Birch Hitting
• 12 year Professional Veteran
• "Training at VT in the off-season had my body feeling the best it felt going into Spring Training. My power in hitting, my speed in running, and the quickness of my feet in the infield hadn’t felt this good in a long time."
• -Teodor Marquist, Professional Baseball Player
• "Dale is one of a handful of baseball-specific strength coaches that we choose to refer out to on the west coast when Halvik Motion Institute athletes are in search of quality supervision and an appreciation for the unique needs of this athletic population."
• Co-Owner of HMI, Gil Ostrander-
• "Having played at the professional level, I understand that the demands of the baseball season are tough and recovery is very important, but also realize the off-season is short and this not just a time to recover but get better."
• - Dale Vantrock Owner

```html
<!DOCTYPE html>
<html lang="en">
<head>
<meta charset="utf-8">
<title>Vantro's Training – Brochure</title>
<link href="https://fonts.googleapis.com/css2?family=Oswald:wght@400;500;600;700&family=Open+Sans:ital,wght@0,400;0,600;0,700;0,800;1,700;1,800&display=swap" rel="stylesheet">
<style>
  :root{
    --blue:#3176b5;
    --blue-deep:#1f4f8c;
    --sky:#33a6d7;
    --ink:#000000;
    --charcoal:#333436;
    --charcoal-dark:#242527;
    --silver:#b2b2b2;
    --paper:#ffffff;
    --paper-soft:#eeeeef;
    --stage:#2c2c2e;
    --condensed:'Oswald', 'Arial Narrow', sans-serif;
    --body:'Open Sans', Arial, sans-serif;
  }
  *{box-sizing:border-box;margin:0;padding:0}
  html,body{width:800px;height:1200px;overflow:hidden;background:var(--stage)}
  .canvas{position:relative;width:800px;height:1200px;overflow:hidden;background:var(--stage);font-family:var(--body)}

  .spread{position:absolute;left:20px;width:760px;height:520px;display:flex;box-shadow:0 10px 30px rgba(0,0,0,.45)}
  .spread--outer{top:40px}
  .spread--inner{top:630px}
  .page{position:relative;width:380px;height:520px;overflow:hidden;background:var(--paper)}
  .page svg.shapes{position:absolute;inset:0;width:380px;height:520px}
  .abs{position:absolute}

  /* Back panel */
  .welcome{left:218px;top:30px;font-family:var(--condensed);color:var(--paper);font-weight:500;line-height:1;text-transform:uppercase;transform:rotate(-12deg);transform-origin:left top}
  .welcome small{display:block;font-size:13px;letter-spacing:.5px}
  .welcome strong{display:block;font-size:25px;font-weight:600}
  .welcome span{display:block;font-size:19px}
  .about{left:30px;top:175px;width:300px;color:var(--paper)}
  .about h2{font-family:var(--body);font-weight:800;font-size:22px;line-height:1.1}
  .rule{display:block;width:40px;height:3px;background:var(--paper);margin:8px 0 10px}
  .about p{font-size:7.6px;line-height:1.45;margin-bottom:5px;opacity:.95}
  .contact{left:170px;top:380px;width:200px;color:var(--paper)}
  .contact h3{font-family:var(--condensed);font-weight:500;font-size:13px;letter-spacing:.5px;margin-bottom:5px}
  .contact li{list-style:none;font-family:var(--condensed);font-size:8px;display:flex;align-items:center;gap:5px;margin-bottom:3px;letter-spacing:.2px}
  .contact svg{width:9px;height:9px;flex:none}
  .social{left:24px;top:478px;display:flex;gap:5px}
  .social i{display:block;width:13px;height:13px;border-radius:50%;background:#55575a}

  /* Cover */
  .slogan{left:28px;top:318px;font-family:var(--condensed);font-weight:700;color:var(--paper);font-size:20px;line-height:1.05;text-transform:uppercase;letter-spacing:.3px}
  .slogan .rule{width:34px;margin-top:10px}
  .brand{left:232px;top:405px;width:140px;text-align:center}
  .brand i{display:block;width:26px;height:26px;background:var(--blue);margin:0 auto 8px}
  .brand span{font-family:var(--condensed);font-weight:600;font-size:17px;color:var(--blue);letter-spacing:.4px;text-transform:uppercase}
  .url-vertical{left:344px;top:250px;font-family:var(--condensed);font-size:8px;color:var(--paper);letter-spacing:.8px;text-transform:uppercase;transform:rotate(90deg);transform-origin:left top;white-space:nowrap}

  /* Inner left */
  .meet{left:28px;top:26px;font-family:var(--body);font-style:italic;font-weight:800;font-size:20px;color:var(--paper);text-transform:uppercase;letter-spacing:-.3px}
  .meet .rule{width:30px;height:3px;margin-top:4px}
  .bio{color:var(--paper);font-size:6.6px;line-height:1.45}
  .bio p{margin-bottom:5px}
  .bio--top{left:28px;top:118px;width:180px}
  .bio--bottom{left:28px;top:262px;width:325px}

  /* Inner right */
  .welcome-in{left:26px;top:32px;width:340px;color:var(--paper)}
  .welcome-in h2{font-style:italic;font-weight:800;font-size:17px;margin-bottom:8px}
  .checks li{list-style:none;font-size:7.4px;line-height:1.6;display:flex;gap:5px;align-items:center}
  .tick{width:8px;height:8px;flex:none}
  .group{left:26px;top:246px;width:335px;color:var(--paper)}
  .group h2{font-style:italic;font-weight:800;font-size:17px;margin-bottom:10px}
  .group h4{font-style:italic;font-weight:700;font-size:7.6px;text-transform:uppercase;margin-bottom:3px}
  .group p{font-size:6.6px;line-height:1.45;margin-bottom:8px;opacity:.92}
  .goals{display:flex;gap:14px;margin:4px 0 10px}
  .goals span{display:flex;align-items:center;gap:4px;font-family:var(--condensed);font-size:11px;letter-spacing:.4px;text-transform:uppercase}
  .goals .tick{width:10px;height:10px}
  .sessions{font-size:6.8px;line-height:1.4}
</style>
</head>
<body>
<div class="canvas">

  <!-- OUTSIDE SPREAD -->
  <section class="spread spread--outer">
    <!-- Back panel -->
    <article class="page page--back">
      <svg class="shapes" viewBox="0 0 380 520" aria-hidden="false">
        <defs>
          <linearGradient id="aboutPhoto" x1="0" y1="0" x2="1" y2="1">
            <stop offset="0" stop-color="#2a5c9c"/>
            <stop offset=".55" stop-color="#1f4f8c"/>
            <stop offset="1" stop-color="#173e72"/>
          </linearGradient>
        </defs>
        <rect width="380" height="520" fill="#ffffff"/>
        <polygon points="0,0 380,0 380,150 0,78" fill="#333436"/>
        <polygon points="0,92 380,166 380,520 215,520 0,430" fill="url(#aboutPhoto)" role="img" aria-label="Blue-toned photo of an athlete training among weight plates"/>
        <polygon points="0,84 380,158 380,162 0,88" fill="#b2b2b2"/>
        <polygon points="0,430 215,520 0,520" fill="#ffffff"/>
        <polygon points="0,422 130,476 130,480 0,426" fill="#b2b2b2"/>
      </svg>

      <div class="abs welcome"><small>Welcome to</small><strong>Vantro's</strong><span>Training</span></div>

      <div class="abs about">
        <h2>About<br>Vantro's Training</h2>
        <span class="rule"></span>
        <p>At Vantro's Training, you will get top level coaching, a great atmosphere, and an individualized program.</p>
        <p>The individualized program is based off an assessment that is done on the first day. The assessment covers mobility, stability, strength, and power.</p>
        <p>Once we have done the assessment, we can build a program of your individual goals and needs.</p>
        <p>Whether you want to take your sports performance to the next level or just feel better, get stronger, and lose body fat, Vantro's Training is for you.</p>
        <p>We take all the guesswork out so all you have to do is come and do the work.</p>
      </div>

      <div class="abs contact">
        <h3>CONTACT US</h3>
        <ul>
          <li><svg viewBox="0 0 10 10"><path d="M5 0.5a3.2 3.2 0 0 0-3.2 3.2C1.8 6 5 9.5 5 9.5S8.2 6 8.2 3.7A3.2 3.2 0 0 0 5 0.5Zm0 4.4a1.2 1.2 0 1 1 0-2.4 1.2 1.2 0 0 1 0 2.4Z" fill="#fff"/></svg>4180 Pinecrest Valley Dr, Pinecrest Valley, CA 90000 USA</li>
          <li><svg viewBox="0 0 10 10"><path d="M2.2 0.8 3.8 2.6 3 3.8C3.6 5 4.9 6.4 6.2 7L7.4 6.2 9.2 7.8 8.2 9.2C4.6 9 1 5.4 0.8 1.8Z" fill="#fff"/></svg>555-410-2276</li>
          <li><svg viewBox="0 0 10 10"><rect x="0.6" y="2" width="8.8" height="6" fill="none" stroke="#fff" stroke-width="1"/><path d="M0.8 2.3 5 5.6 9.2 2.3" fill="none" stroke="#fff" stroke-width="1"/></svg>dale@dalevantrock.example</li>
          <li><svg viewBox="0 0 10 10"><circle cx="5" cy="5" r="4.2" fill="none" stroke="#fff" stroke-width="1"/><path d="M0.8 5H9.2M5 0.8C3 3 3 7 5 9.2M5 0.8C7 3 7 7 5 9.2" fill="none" stroke="#fff" stroke-width=".8"/></svg>www.vantrostraining.example</li>
        </ul>
      </div>

      <div class="abs social" aria-hidden="true"><i></i><i></i><i></i></div>
    </article>

    <!-- Front cover -->
    <article class="page page--cover">
      <svg class="shapes" viewBox="0 0 380 520">
        <defs>
          <linearGradient id="coverPhoto" x1="0" y1="0" x2="1" y2="1">
            <stop offset="0" stop-color="#c9d3e6"/>
            <stop offset=".5" stop-color="#6f7fa8"/>
            <stop offset="1" stop-color="#2c2f3a"/>
          </linearGradient>
        </defs>
        <rect width="380" height="520" fill="#eeeeef"/>
        <polygon points="0,0 332,0 332,282 0,208" fill="url(#coverPhoto)" role="img" aria-label="Photo of an athlete deadlifting a loaded barbell beside a blue squat rack"/>
        <polygon points="380,118 380,372 236,300" fill="#3176b5"/>
        <polygon points="0,222 300,290 185,520 0,520" fill="#333436"/>
        <polygon points="250,318 380,384 380,520 200,520" fill="#ffffff"/>
        <line x1="0" y1="216" x2="310" y2="286" stroke="#b2b2b2" stroke-width="2"/>
      </svg>

      <div class="abs url-vertical">www.vantrostraining.example</div>

      <div class="abs slogan">Move Better<br>Feel Better<br>Be Better<span class="rule"></span></div>

      <div class="abs brand"><i></i><span>Vantro's Training</span></div>
    </article>
  </section>

  <!-- INSIDE SPREAD -->
  <section class="spread spread--inner">
    <!-- Meet Dale -->
    <article class="page page--meet">
      <svg class="shapes" viewBox="0 0 380 520">
        <defs>
          <linearGradient id="portrait" x1="0" y1="0" x2="0" y2="1">
            <stop offset="0" stop-color="#e8e8e8"/>
            <stop offset="1" stop-color="#8a8a8a"/>
          </linearGradient>
          <linearGradient id="bandPhoto" x1="0" y1="0" x2="1" y2="1">
            <stop offset="0" stop-color="#d9d7cf"/>
            <stop offset=".45" stop-color="#4f8a5a"/>
            <stop offset="1" stop-color="#5a6470"/>
          </linearGradient>
        </defs>
        <rect width="380" height="520" fill="#ffffff"/>
        <path d="M0,112 Q190,52 380,70 V520 H0 Z" fill="#333436"/>
        <path d="M0,22 Q180,0 380,18 V70 Q190,52 0,112 Z" fill="#3176b5"/>
        <rect x="214" y="78" width="142" height="172" rx="4" fill="url(#portrait)" role="img" aria-label="Black and white portrait of the head coach holding his twin babies"/>
        <path d="M0,395 Q180,330 380,352 V520 H0 Z" fill="url(#bandPhoto)" role="img" aria-label="Photo of a coach in a green shirt doing a resistance band exercise"/>
        <path d="M220,372 Q300,346 380,352 V366 Q300,362 240,380 Z" fill="#3176b5"/>
      </svg>

      <div class="abs meet">Meet Dale<span class="rule"></span></div>

      <div class="abs bio bio--top">
        <p>Hey, I'm Dale Vantrock, the President of Vantro's Training. I'm a Certified Personal Trainer and Performance Enhancement Specialist through the National Council of Motion Science. I started my career as a professional baseball player, where I spent my off-seasons training, getting ready to be at my best for each season ahead. After several seasons of professional baseball, I decided to change my focus from playing baseball to training other athletes. I started training in 2013 in my brother-in-law's garage and then expanded to my own facility in Pinecrest Valley, CA.</p>
        <p>Having played pro baseball, I know what it requires to be able to get your body to perform at its best when you step into competition.</p>
      </div>
      <div class="abs bio bio--bottom">
        <p>Baseball was my passion, now my drive is helping athletes perform at the top of their game. I love watching my athletes take their results from the gym to their sport.</p>
        <p>I also enjoy helping people feel their best. Whether it's helping people lose fat, build muscle, or getting stronger, I take pride in helping people feel their best. I am dedicated to my clients, their goals and helping them develop into their fitness needs.</p>
        <p>In 2014, my wife and I became the parents of twins, Owen and Lucas. When I am not in the gym, either training clients or working out myself, I am very busy with them. In addition to spending time with my family I enjoy watching all kinds of sports and especially watching my athletes compete and do their best.</p>
      </div>
    </article>

    <!-- Welcome / Group Strength -->
    <article class="page page--program">
      <svg class="shapes" viewBox="0 0 380 520">
        <defs>
          <linearGradient id="gymPhoto" x1="0" y1="0" x2="1" y2="1">
            <stop offset="0" stop-color="#4a4c50"/>
            <stop offset=".6" stop-color="#2e2f32"/>
            <stop offset="1" stop-color="#1d1e20"/>
          </linearGradient>
        </defs>
        <rect width="380" height="520" fill="#ffffff"/>
        <path d="M0,228 Q190,182 380,196 V520 H0 Z" fill="url(#gymPhoto)" role="img" aria-label="Dimmed photo of a group training session in the gym"/>
        <path d="M0,36 Q200,4 380,12 V182 Q190,168 0,214 Z" fill="#3176b5"/>
        <path d="M0,214 Q190,168 380,182 V188 Q190,176 0,222 Z" fill="#b2b2b2"/>
        <polygon points="330,470 380,440 380,520 300,520" fill="#3176b5" opacity=".85"/>
      </svg>

      <div class="abs welcome-in">
        <h2>Welcome To Vantro's Training</h2>
        <ul class="checks">
          <li><svg class="tick" viewBox="0 0 10 10"><path d="M1 5.5 4 8.5 9 1.5" fill="none" stroke="#fff" stroke-width="1.6"/></svg>Are you looking for an individualized program based off your own needs?</li>
          <li><svg class="tick" viewBox="0 0 10 10"><path d="M1 5.5 4 8.5 9 1.5" fill="none" stroke="#fff" stroke-width="1.6"/></svg>Are you ready to take your sports performance to the next level?</li>
          <li><svg class="tick" viewBox="0 0 10 10"><path d="M1 5.5 4 8.5 9 1.5" fill="none" stroke="#fff" stroke-width="1.6"/></svg>Do you want to Move Better, Feel Better, Be Better?</li>
          <li><svg class="tick" viewBox="0 0 10 10"><path d="M1 5.5 4 8.5 9 1.5" fill="none" stroke="#fff" stroke-width="1.6"/></svg>Do you want to burn fat, build muscle, and get stronger?</li>
          <li><svg class="tick" viewBox="0 0 10 10"><path d="M1 5.5 4 8.5 9 1.5" fill="none" stroke="#fff" stroke-width="1.6"/></svg>Do you want to train with people like you, who want to get better?</li>
          <li><svg class="tick" viewBox="0 0 10 10"><path d="M1 5.5 4 8.5 9 1.5" fill="none" stroke="#fff" stroke-width="1.6"/></svg>Do you want to be part of the Vantro's Training family?</li>
        </ul>
      </div>

      <div class="abs group">
        <h2>Vantro's Group Strength</h2>
        <h4>Adult Strength</h4>
        <p>This program focuses on adult fitness as it enhances all aspects of training, from mobility, to agility, to power, these characteristics will be fully improved throughout our sessions. With the help from our coaches, you will receive guidance and support throughout every training session.</p>
        <h4>Weekly Challenges &amp; Monthly Focuses</h4>
        <p>We want our program to be effective so we have designed weekly challenges and monthly focuses for our members. You can participate in weekly competitions with other gym members as well as setting goals each month. With our help you will succeed in achieving your goals and challenging yourself to the fullest.</p>
        <h4>Vantro's Goal</h4>
        <div class="goals">
          <span><svg class="tick" viewBox="0 0 10 10"><path d="M1 5.5 4 8.5 9 1.5" fill="none" stroke="#fff" stroke-width="1.4"/></svg>Strength</span>
          <span><svg class="tick" viewBox="0 0 10 10"><path d="M1 5.5 4 8.5 9 1.5" fill="none" stroke="#fff" stroke-width="1.4"/></svg>Power</span>
          <span><svg class="tick" viewBox="0 0 10 10"><path d="M1 5.5 4 8.5 9 1.5" fill="none" stroke="#fff" stroke-width="1.4"/></svg>Mobility</span>
          <span><svg class="tick" viewBox="0 0 10 10"><path d="M1 5.5 4 8.5 9 1.5" fill="none" stroke="#fff" stroke-width="1.4"/></svg>Confidence</span>
        </div>
        <h4>Sessions</h4>
        <p class="sessions">Monday, Wednesday, Friday<br>Times: 6:30 am, 7:30 am, or 8:30 am</p>
      </div>
    </article>
  </section>

</div>
</body>
</html>
```